Progressive/contemporary business card design for successful Startups as a Service Company

New logo launched in 2020. New website launched in 2021. Now that COVID is (mostly) behind us, I'm networking with more people and need a business card that matches the company/logo design aesthetic.

```html
<!DOCTYPE html>
<html lang="en">
<head>
<meta charset="utf-8">
<title>Brightway Business Card</title>
<link href="https://fonts.googleapis.com/css2?family=Montserrat:wght@300;400;500&display=swap" rel="stylesheet">
<style>
  :root {
    --bg: #e9e9ea;
    --card: #ffffff;
    --ink: #3f4a5e;
    --muted: #9b9b9b;
    --blue: #1b8fd6;
    --sky: #35bdee;
    --yellow: #fdc514;
    --orange: #f58a1f;
    --red: #ec2a26;
    --green: #5bb847;
    --lime: #a9cf3a;
    --purple: #7d2a8a;
    --magenta: #ec0f8c;
    --icon-phone: #1e9ad6;
    --icon-mail: #3fae49;
    --icon-home: #f26522;
  }
  * { margin: 0; padding: 0; box-sizing: border-box; }
  html, body {
    width: 1200px; height: 583px; overflow: hidden;
    background: var(--bg);
    font-family: "Montserrat", sans-serif;
  }
  .stage { position: relative; width: 1200px; height: 583px; }
  .card {
    position: absolute; top: 137px;
    width: 515px; height: 309px;
    background: var(--card);
    box-shadow: 0 6px 14px rgba(0,0,0,0.18);
    overflow: hidden;
  }
  .card--front { left: 68px; }
  .card--back { left: 622px; }

  .brand-block {
    position: absolute; top: 0; height: 100%;
  }
  .card--front .brand-block {
    right: 0; width: 158px;
    background: linear-gradient(180deg, var(--blue) 0%, var(--yellow) 32%, var(--orange) 50%, var(--red) 68%, var(--green) 88%, var(--lime) 100%);
  }
  .card--back .brand-block {
    left: 0; width: 154px;
    background: linear-gradient(180deg, var(--sky) 0%, var(--blue) 22%, var(--purple) 45%, var(--magenta) 70%, var(--green) 100%);
  }

  .wordmark {
    position: absolute;
    color: var(--ink);
    font-weight: 400;
    line-height: 1;
    white-space: nowrap;
  }
  .card--front .wordmark { left: 40px; top: 138px; font-size: 36px; letter-spacing: 0.12em; }
  .card--back .wordmark { left: 201px; top: 84px; font-size: 22px; letter-spacing: 0.14em; }

  .person { position: absolute; left: 201px; top: 138px; }
  .person__name {
    color: var(--ink); font-weight: 300; font-size: 23px; line-height: 1;
  }
  .person__role {
    color: var(--muted); font-weight: 300; font-size: 12.5px; margin-top: 1px;
  }
  .contacts { list-style: none; margin-top: 5px; }
  .contacts li {
    display: flex; align-items: center; gap: 6px;
    color: var(--muted); font-weight: 300; font-size: 12.5px;
    height: 18.5px; white-space: nowrap;
  }
  .contacts svg { width: 11px; height: 11px; flex: none; }
</style>
</head>
<body>
<div class="stage">
  <section class="card card--front">
    <div class="wordmark">BRIGHTWAY</div>
    <div class="brand-block" role="img" aria-label="Colourful geometric brand pattern"></div>
  </section>

  <section class="card card--back">
    <div class="brand-block" role="img" aria-label="Colourful geometric brand pattern"></div>
    <div class="wordmark">BRIGHTWAY</div>
    <div class="person">
      <div class="person__name">JOHN DOE</div>
      <div class="person__role">Mangaer</div>
      <ul class="contacts">
        <li>
          <svg viewBox="0 0 12 12" aria-hidden="true"><circle cx="6" cy="6" r="6" fill="var(--icon-phone)"/><path d="M4 3.2c.4-.3.8-.2 1 .2l.4.8c.1.3 0 .5-.2.7l-.3.3c.3.7.9 1.3 1.6 1.6l.3-.3c.2-.2.5-.3.7-.2l.8.4c.4.2.5.6.2 1l-.4.4C6.5 8.6 3.4 5.5 3.6 3.6z" fill="#fff"/></svg>
          555-013-247
        </li>
        <li>
          <svg viewBox="0 0 12 12" aria-hidden="true"><circle cx="6" cy="6" r="6" fill="var(--icon-mail)"/><rect x="3" y="4" width="6" height="4.2" rx=".4" fill="#fff"/><path d="M3.2 4.3 6 6.3l2.8-2" stroke="var(--icon-mail)" stroke-width=".7" fill="none"/></svg>
          hello@brightwaylabs.com
        </li>
        <li>
          <svg viewBox="0 0 12 12" aria-hidden="true"><circle cx="6" cy="6" r="6" fill="var(--icon-home)"/><path d="M6 2.8 9 5.5H8.2v3.2H3.8V5.5H3z" fill="#fff"/><rect x="5.3" y="6.4" width="1.4" height="2.3" fill="var(--icon-home)"/></svg>
          14 Harbor Lane, Norwood, box 40215
        </li>
      </ul>
    </div>
  </section>
</div>
</body>
</html>
```